tilebarnowl.net needs a cool website!

I need a website designed for a commercial flooring maintenance company based in Texas. We will be providing services like carpet shampooing, burnishing, resurfacing and power washing. It needs to be cool and trendy.

I’ll need 10-20 pages. I need help deciding on the style and color palette. We will need great stock pictures of different flooring types and you will need to photo shop our logo on imaginary cars or storefronts.

Please have similar experience and an open mind. I’m looking for a partnership and someone to turn to for future projects and upkeep.

The domain is currently hosted on Wix. You will need the ability to develop and code it there.

Target Market(s)

Commercial businesses and properties

Industry/Entity Type

Floor care

Coding

Coded - Design and coding required

Number of Pages Required

5+ page

Requirements
Must have
• Great pictures of different types of floors.

```html
<!DOCTYPE html>
<html lang="en">
<head>
<meta charset="utf-8">
<title>Tilebarnowl – Commercial Flooring Maintenance</title>
<link rel="stylesheet" href="https://fonts.googleapis.com/css2?family=Roboto:wght@300;400;500;700;900&family=Roboto+Condensed:wght@700&family=Open+Sans:wght@400;600&display=swap">
<style>
:root{
  --green:#6aa72e;
  --green-dark:#4f8a1f;
  --green-band:#5b9a25;
  --ink:#111;
  --text:#444;
  --muted:#777;
  --dark:#232323;
  --soft:#f1f3f6;
  --white:#fff;
  --line:#dde1e6;
}
*{box-sizing:border-box;margin:0;padding:0}
html,body{width:1200px;height:5111px;overflow:hidden}
body{position:relative;font-family:"Open Sans",sans-serif;color:var(--text);background:var(--white)}
.btn{position:absolute;display:flex;align-items:center;justify-content:center;background:var(--green);color:var(--white);font:500 13px "Roboto",sans-serif;letter-spacing:.4px;text-transform:uppercase;border-radius:2px}
.eyebrow{position:absolute;left:0;width:1200px;text-align:center;font:400 15px "Roboto",sans-serif;color:var(--green);text-transform:uppercase}
.heading{position:absolute;left:0;width:1200px;text-align:center;font:700 44px "Roboto Condensed",sans-serif;color:var(--ink);text-transform:uppercase}
.sub{position:absolute;text-align:center;font:400 15px/26px "Open Sans",sans-serif;color:#333}
.photo{position:absolute}

/* hero */
.hero{position:absolute;left:0;top:0;width:1200px;height:760px;clip-path:polygon(0 0,100% 0,100% 575px,476px 760px,0 645px);
  background:linear-gradient(100deg,#3a2a1e 0%,#5d4530 30%,#7b6a57 55%,#3d6f8f 75%,#9aa3a8 100%)}
.hero-shade{position:absolute;inset:0;background:linear-gradient(90deg,rgba(0,0,0,.55),rgba(0,0,0,.1) 60%,rgba(0,0,0,0))}
.logo{position:absolute;display:flex;align-items:center;gap:8px;font:400 30px "Open Sans",sans-serif;letter-spacing:-.5px}
.logo .dot{width:12px;height:12px;border-radius:50%;background:var(--green)}
.nav{position:absolute;top:26px;font:500 14px "Roboto",sans-serif;color:var(--white)}
.nav.active{color:var(--green)}
.hero h2{position:absolute;left:66px;top:212px;font:300 30px "Roboto",sans-serif;color:var(--white)}
.hero h1{position:absolute;left:66px;top:252px;font:700 44px/56px "Roboto",sans-serif;color:var(--white)}
.hero p{position:absolute;left:66px;top:396px;width:470px;font:400 15px/26px "Open Sans",sans-serif;color:var(--white)}

/* partners */
.partners-title{position:absolute;left:0;top:844px;width:1200px;text-align:center;font:400 24px "Roboto",sans-serif;color:var(--ink)}
.partner{position:absolute;top:938px;display:flex;align-items:center;gap:6px;font:600 19px "Open Sans",sans-serif;color:#666}
.partner .sq{width:14px;height:14px;background:#777}

/* welcome */
.welcome{position:absolute;left:0;top:1059px;width:1200px;height:642px;background:var(--dark);clip-path:polygon(0 0,100% 0,100% 309px,594px 531px,0 335px)}
.video{left:66px;top:1128px;width:589px;height:404px;border-radius:12px;background:linear-gradient(150deg,#6c7176 0%,#8a8e90 45%,#bcbcb8 100%);box-shadow:0 30px 40px -20px rgba(0,0,0,.45)}
.play{position:absolute;left:332px;top:1302px;width:54px;height:54px;border-radius:50%;border:2px solid var(--white)}
.welcome-eyebrow{position:absolute;left:714px;top:1166px;font:400 15px "Roboto",sans-serif;color:var(--green)}
.welcome-title{position:absolute;left:714px;top:1196px;font:700 40px "Roboto",sans-serif;color:var(--white)}
.welcome-text{position:absolute;left:714px;top:1276px;width:430px;font:400 14px/26px "Open Sans",sans-serif;color:#ddd}

/* services */
.services-band{position:absolute;left:0;top:1701px;width:1200px;height:407px;background:linear-gradient(135deg,#4e8a1e,#6aa72e)}
.service-img{top:1938px;width:344px;height:324px;border-radius:12px}
.service-card{position:absolute;top:2200px;width:301px;height:216px;background:var(--white);border-radius:8px;box-shadow:0 8px 24px rgba(0,0,0,.12);text-align:center}
.service-card h3{margin-top:20px;font:500 21px "Roboto",sans-serif;color:var(--ink)}
.service-card p{margin:10px auto 0;width:260px;font:400 13px/23px "Open Sans",sans-serif;color:#555}
.service-card .btn{left:73px;top:148px;width:155px;height:44px}

/* projects */
.tile{position:absolute}
.overlay{position:absolute;left:66px;top:2919px;width:349px;height:223px;background:rgba(76,130,30,.82);color:var(--white);text-align:center}
.overlay h4{margin-top:82px;font:500 16px "Roboto",sans-serif;letter-spacing:.5px}
.overlay p{margin-top:8px;font:400 13px "Open Sans",sans-serif}

/* testimonials */
.testi-band{position:absolute;left:0;top:3232px;width:1200px;height:420px;background:var(--soft)}
.testi{position:absolute;top:3428px;width:522px;height:208px;background:var(--white);border-radius:8px;box-shadow:0 4px 16px rgba(0,0,0,.05)}
.avatar{position:absolute;left:0;top:0;width:176px;height:176px;border-radius:50% 50% 50% 0}
.testi blockquote{position:absolute;left:198px;top:36px;width:300px;font:italic 400 13.5px/24px "Open Sans",sans-serif;color:#555}
.testi .name{position:absolute;left:198px;top:152px;font:600 13px "Roboto",sans-serif;color:var(--ink)}
.testi .role{position:absolute;left:198px;top:170px;font:400 11px "Open Sans",sans-serif;color:#777}

/* contact */
.contact-photo{left:0;top:4236px;width:1200px;height:464px;background:linear-gradient(90deg,#7a5a3c 0%,#b68a5b 25%,#8a6c50 50%,#4e6270 75%,#7e5d3d 100%)}
.form-card{position:absolute;left:334px;top:3852px;width:532px;height:568px;background:var(--white);border-radius:10px;box-shadow:0 6px 30px rgba(0,0,0,.1)}
.form-card .intro{position:absolute;left:26px;top:36px;width:480px;text-align:center;font:400 15px/26px "Open Sans",sans-serif;color:#333}
.field{position:absolute;left:33px;width:466px;height:46px;border:1px solid var(--line);display:flex;align-items:center;justify-content:space-between;padding:0 20px 0 14px;font:400 11.5px "Open Sans",sans-serif;color:#666}
.field.filled{background:#eef6e4;border-color:#cde3b4;color:#333}
.field svg{width:14px;height:14px;stroke:#777;fill:none;stroke-width:1.6}
.field.message{height:128px;align-items:flex-start;padding-top:14px}

/* footer */
.footer-text{position:absolute;left:66px;top:4882px;width:330px;font:400 13px/22px "Open Sans",sans-serif;color:#333}
.fcol-title{position:absolute;top:4784px;font:600 13px "Roboto",sans-serif;color:var(--green);text-transform:uppercase}
.fcol-title::after{content:"";position:absolute;left:0;top:20px;width:38px;height:2px;background:var(--green)}
.flink{position:absolute;font:400 13px "Open Sans",sans-serif;color:#333}
.ficon{position:absolute;left:888px;width:36px;height:36px;border-radius:50%;border:1.5px solid var(--green);display:flex;align-items:center;justify-content:center}
.ficon svg{width:16px;height:16px;stroke:var(--green);fill:none;stroke-width:1.8}
.rule{position:absolute;left:66px;top:5060px;width:1068px;height:1px;background:#e3e3e3}
.social{position:absolute;top:5074px;width:32px;height:32px;border-radius:50%;border:1.5px solid #333}
.social.on{background:var(--green);border-color:var(--green)}
.copyright{position:absolute;right:66px;top:5083px;font:400 12px "Open Sans",sans-serif;color:#333}
.copyright span{color:var(--green)}
</style>
</head>
<body>

<!-- Hero -->
<section class="hero">
  <div role="img" aria-label="Technician in blue uniform running a floor scrubber machine in a modern office" style="position:absolute;inset:0"></div>
  <div class="hero-shade"></div>
  <div class="logo" style="left:66px;top:16px;color:var(--white)"><span class="dot"></span>tilebarnowl</div>
  <span class="nav active" style="left:424px">Home</span>
  <span class="nav" style="left:520px">About Us</span>
  <span class="nav" style="left:640px">Services</span>
  <span class="nav" style="left:755px">Projects</span>
  <span class="nav" style="left:868px">Contact Us</span>
  <span class="btn" style="left:975px;top:14px;width:158px;height:44px">Get a Quote</span>
  <h2>Commercial</h2>
  <h1>Flooring Maintenance<br>Company</h1>
  <p>Nor again is there anyone who loves or pursues or desires to obtain pain of itself</p>
  <span class="btn" style="left:66px;top:490px;width:162px;height:44px">Get Started</span>
</section>

<!-- Partners -->
<div class="partners-title">Companies We Have Work With</div>
<div class="partner" style="left:88px"><span class="sq"></span>Northgate Labs</div>
<div class="partner" style="left:278px">Quillmark</div>
<div class="partner" style="left:460px">Keystep</div>
<div class="partner" style="left:648px">Tripvane</div>
<div class="partner" style="left:830px"><span class="sq" style="border-radius:50%"></span>Nestly</div>
<div class="partner" style="left:1004px"><span class="sq"></span>Tallyo</div>

<!-- Welcome -->
<section class="welcome"></section>
<div class="photo video" role="img" aria-label="Worker kneeling and levelling large floor tiles in a warehouse"></div>
<div class="play"><svg width="50" height="50" viewBox="0 0 50 50"><path d="M21 17 L33 25 L21 33 Z" fill="#fff"/></svg></div>
<div class="welcome-eyebrow">WELCOME TO</div>
<div class="welcome-title">TILEBARNOWL</div>
<p class="welcome-text">Nor again is there anyone who loves or pursues or desires to obtain pain of itself, because it is pain, but because occasionally circumstances occur in which toil and pain can procure him some great pleasure take a trivial example, which of us ever undertakes...</p>
<span class="btn" style="left:714px;top:1444px;width:156px;height:44px">Read More</span>

<!-- Services -->
<section class="services-band"></section>
<div class="eyebrow" style="top:1752px;color:#b9dc8f">What We Do</div>
<div class="heading" style="top:1780px;color:var(--white)">Our Services We Offer</div>
<div class="sub" style="left:0;top:1843px;width:1200px;color:#eaf4dc;font-size:14px">To take a trivial example, which of us ever undertakes laborious physical exercise, except to obtain some advantage from it</div>

<div class="photo service-img" style="left:66px;background:linear-gradient(180deg,#3a6f9c,#2d86a8 50%,#c24a3a)" role="img" aria-label="Carpet shampooing machine on a colourful carpet"></div>
<div class="photo service-img" style="left:427px;background:linear-gradient(180deg,#4a5870,#c86a2e 45%,#8fa0b4)" role="img" aria-label="Burnishing machine polishing a glossy floor"></div>
<div class="photo service-img" style="left:790px;background:linear-gradient(180deg,#d8dde2,#aab2ba 55%,#7e8792)" role="img" aria-label="Yellow power washer in an industrial plant"></div>

<div class="service-card" style="left:87px"><h3>Carpet Shampooing</h3><p>Quis autem vel eum iure reprehenderit qui in ea voluptate velit esse quam</p><span class="btn">Read More</span></div>
<div class="service-card" style="left:450px"><h3>Burnishing</h3><p>Quis autem vel eum iure reprehenderit qui in ea voluptate velit esse quam</p><span class="btn">Read More</span></div>
<div class="service-card" style="left:812px"><h3>Power Washing</h3><p>Quis autem vel eum iure reprehenderit qui in ea voluptate velit esse quam</p><span class="btn">Read More</span></div>

<!-- Projects -->
<div class="eyebrow" style="top:2503px">Projects</div>
<div class="heading" style="top:2530px">Different Flooring</div>
<div class="sub" style="left:240px;top:2598px;width:720px">To take a trivial example, which of us ever undertakes laborious physical exercise, except to obtain some advantage from it</div>

<div class="tile" style="left:66px;top:2685px;width:349px;height:223px;background:linear-gradient(180deg,#3b3633,#b79f7f 55%,#d4bc98)" role="img" aria-label="Glass meeting rooms with light wooden floor"></div>
<div class="tile" style="left:426px;top:2685px;width:348px;height:457px;background:linear-gradient(180deg,#e7e7e3,#cfcfca 50%,#7e7a70)" role="img" aria-label="Corridor with striped grey carpet and black lounge chairs"></div>
<div class="tile" style="left:785px;top:2685px;width:349px;height:223px;background:linear-gradient(180deg,#3d3a3a,#6f5a4a 50%,#5c7aa0)" role="img" aria-label="Hotel hallway with patterned carpet"></div>
<div class="tile" style="left:66px;top:2919px;width:349px;height:223px;background:linear-gradient(180deg,#5e6d52,#8a9a7a)" role="img" aria-label="Office interior with flooring"></div>
<div class="overlay"><h4>TEMPORA INCIDUNT</h4><p>Duis aute irure dolor in reprehenderit voluptate</p></div>
<div class="tile" style="left:785px;top:2919px;width:349px;height:223px;background:linear-gradient(180deg,#c9cfd2,#9aa8ae 50%,#5f9a3a)" role="img" aria-label="Open office with green carpet flooring"></div>

<!-- Testimonials -->
<section class="testi-band"></section>
<div class="eyebrow" style="top:3282px">Testimonials</div>
<div class="heading" style="top:3310px">What Our Customer Says</div>

<div class="testi" style="left:66px">
  <div class="avatar" role="img" aria-label="Portrait of a smiling customer" style="background:linear-gradient(135deg,#f0b23a,#e59a1e)"></div>
  <blockquote>“To take a trivial example, which of us ever undertakes laborious physical exercise, except to obtain some advantage But who has any right to find fault with a man”...</blockquote>
  <div class="name">DARREN HOLLIS</div><div class="role">Designer</div>
</div>
<div class="testi" style="left:611px">
  <div class="avatar" role="img" aria-label="Portrait of a smiling customer" style="background:linear-gradient(135deg,#e9e3dc,#d49a3e)"></div>
  <blockquote>“To take a trivial example, which of us ever undertakes laborious physical exercise, except to obtain some advantage But who has any right to find fault with a man”...</blockquote>
  <div class="name">MARISA VENTO</div><div class="role">Designer</div>
</div>

<!-- Contact -->
<div class="eyebrow" style="top:3742px">Contact Us</div>
<div class="heading" style="top:3770px">Get in Touch With Us</div>
<div class="photo contact-photo" role="img" aria-label="Cleaner operating a floor scrubber in a bright glass lobby"></div>

<form class="form-card">
  <p class="intro">To take a trivial example, which of us ever undertakes laborious physical exercise except to obtain some advantage...</p>
  <div class="field filled" style="top:121px">Nolan Pryce |<svg viewBox="0 0 16 16"><circle cx="8" cy="5" r="3"/><path d="M2 15c0-3.5 2.7-5 6-5s6 1.5 6 5"/></svg></div>
  <div class="field" style="top:184px">Email address<svg viewBox="0 0 16 16"><rect x="1.5" y="3" width="13" height="10" rx="1"/><path d="M2 4l6 5 6-5"/></svg></div>
  <div class="field" style="top:246px">Phone number<svg viewBox="0 0 16 16"><path d="M3 2h3l1.5 3.5-2 1.2a8 8 0 0 0 3.8 3.8l1.2-2L14 10v3a1 1 0 0 1-1 1A12 12 0 0 1 2 3a1 1 0 0 1 1-1z"/></svg></div>
  <div class="field" style="top:308px">Services<svg viewBox="0 0 16 16"><path d="M4 6l4 4 4-4"/></svg></div>
  <div class="field message" style="top:370px">Message<svg viewBox="0 0 16 16"><path d="M3 13l1-4 7-7 3 3-7 7z"/></svg></div>
  <span class="btn" style="left:188px;top:508px;width:156px;height:44px">Send Now</span>
</form>

<!-- Footer -->
<div class="logo" style="left:66px;top:4808px;color:var(--ink);font-size:40px"><span class="dot" style="width:16px;height:16px"></span>tilebarnowl</div>
<p class="footer-text">Quis autem vel eum iure reprehenderit qui in ea voluptate velit esse quam nihil molestiae consequatur, vel illum qui dolorem eum fugiat quo voluptas nulla pariatur</p>

<div class="fcol-title" style="left:488px">Quick Links</div>
<span class="flink" style="left:488px;top:4820px">Home</span>
<span class="flink" style="left:488px;top:4854px">About Us</span>
<span class="flink" style="left:488px;top:4888px">Services</span>
<span class="flink" style="left:488px;top:4922px">Projects</span>
<span class="flink" style="left:488px;top:4956px">Contact Us</span>

<div class="fcol-title" style="left:672px">Services</div>
<span class="flink" style="left:672px;top:4820px">Carpet Shampooing</span>
<span class="flink" style="left:672px;top:4854px">Burnishing</span>
<span class="flink" style="left:672px;top:4888px">Resurfacing</span>
<span class="flink" style="left:672px;top:4922px">Power washing</span>

<div class="fcol-title" style="left:888px">Contact Us</div>
<div class="ficon" style="top:4820px"><svg viewBox="0 0 16 16"><path d="M8 15s5-5 5-9a5 5 0 0 0-10 0c0 4 5 9 5 9z"/><circle cx="8" cy="6" r="1.8"/></svg></div>
<span class="flink" style="left:934px;top:4818px;line-height:20px">41 Harbor Row Suite 7<br>Millbrook 48QRT USA</span>
<div class="ficon" style="top:4876px"><svg viewBox="0 0 16 16"><path d="M3 2h3l1.5 3.5-2 1.2a8 8 0 0 0 3.8 3.8l1.2-2L14 10v3a1 1 0 0 1-1 1A12 12 0 0 1 2 3a1 1 0 0 1 1-1z"/></svg></div>
<span class="flink" style="left:934px;top:4885px">+1 (555) 204 7731</span>
<div class="ficon" style="top:4932px"><svg viewBox="0 0 16 16"><rect x="1.5" y="3" width="13" height="10" rx="1"/><path d="M2 4l6 5 6-5"/></svg></div>
<span class="flink" style="left:934px;top:4941px;color:var(--green)">info@tilebarnowl.net</span>

<div class="rule"></div>
<span class="social on" style="left:68px"></span>
<span class="social" style="left:114px"></span>
<span class="social" style="left:159px"></span>
<span class="social" style="left:204px"></span>
<div class="copyright">© <span>Tilebarnowl</span>, 2024. All Rights Reserved.</div>

</body>
</html>
```